Martin Hale PA Card Logo

Current logo attached. Its 25 year old logo I have used. Looking for a new fresh elegant professional look/design for a law firm that has high net worth clientele and is estate planning business law firm. Firm mis in Palm Beach Florida.
One sided card linen stock white will be used. Logo section name section. Logo should include nice elegant design using the letter "M" perhapa (I am not wed to current font of the M on current logo.) Be creative there with logo design. My initials are MH.......color scheme I figure 3 tone... Raised Gold Foil, Blue name of firm = Martin Hale, P.A. My practice focus is Family and Business Asset Protection. My name is Martin M. Hale, Esq. Practice specialties include Asset Protection trusts, Business Succession Planning, LLC law, Estate Planning, Medicaid Planning (Maybe put those topics in bullets in a section of card. Bottom of card can be reserved smaller print address phone website and email address. Address section is not as important as logo and topics of practice on front. I foresee address section can be in dark blue. MY name and Topics dark blue as well.
Target Market(s)
affluent; business owners executives; wealth 2-10 million net worth
Industry/Entity Type
business law and estate planning
Contact Information for Business Card
White thick linen one sided

```html
<!DOCTYPE html>
<html lang="en">
<head>
<meta charset="utf-8">
<title>Martin Hale PA Card</title>
<link href="https://fonts.googleapis.com/css2?family=Marcellus&family=Questrial&display=swap" rel="stylesheet">
<style>
  :root {
    --stage: #ececec;
    --stage-low: #ffffff;
    --card: #fbfbfa;
    --ink-dark: #1c1c1e;
    --brand-blue: #0f52a8;
    --navy: #1d3a8a;
    --rule: #7aa0cf;
  }
  * { margin: 0; padding: 0; box-sizing: border-box; }
  html, body { width: 1200px; height: 1200px; overflow: hidden; }
  body {
    background: linear-gradient(var(--stage) 0 66%, var(--stage-low) 66% 100%);
    position: relative;
    font-family: "Marcellus", serif;
  }
  .card {
    position: absolute;
    left: 150px; top: 90px;
    width: 900px; height: 514px;
    background: var(--card);
    box-shadow: 0 18px 40px rgba(0,0,0,0.16), 0 2px 6px rgba(0,0,0,0.08);
  }
  .card__mark {
    position: absolute;
    left: 90px; top: 128px;
    width: 104px; height: 104px;
    background: var(--brand-blue);
  }
  .card__name {
    position: absolute;
    left: 218px; top: 126px;
    font-size: 48px;
    letter-spacing: 3px;
    color: var(--ink-dark);
    line-height: 1;
    white-space: nowrap;
  }
  .card__tagline {
    position: absolute;
    left: 232px; top: 190px;
    font-size: 15px;
    letter-spacing: 5px;
    color: var(--brand-blue);
    text-transform: uppercase;
    white-space: nowrap;
  }
  .card__services {
    position: absolute;
    left: 90px; top: 282px;
    color: var(--navy);
    font-size: 23px;
    letter-spacing: 0.5px;
    line-height: 1.25;
    text-transform: uppercase;
    list-style: none;
  }
  .card__services li { white-space: nowrap; }
  .card__services li:nth-child(2) { padding-left: 52px; }
  .sep { margin: 0 14px; }
  .card__rule {
    position: absolute;
    left: 90px; right: 90px; top: 392px;
    border-top: 1px solid var(--rule);
  }
  .card__contact {
    position: absolute;
    left: 90px; top: 420px;
    font-family: "Questrial", sans-serif;
    font-size: 13.5px;
    color: var(--navy);
    letter-spacing: 0.3px;
    white-space: nowrap;
  }
  .mark-display {
    position: absolute;
    left: 0; right: 0; top: 880px;
    display: flex;
    justify-content: center;
    align-items: center;
    gap: 28px;
  }
  .mark-display__square {
    width: 210px; height: 210px;
    background: var(--brand-blue);
  }
  .mark-display__initials {
    font-size: 96px;
    color: var(--brand-blue);
    letter-spacing: 6px;
    line-height: 1;
  }
</style>
</head>
<body>
  <section class="card" aria-label="Business card front">
    <div class="card__mark"></div>
    <h1 class="card__name">MARTIN HALE P.A.</h1>
    <p class="card__tagline">Family &amp; Business Asset Protection</p>
    <ul class="card__services">
      <li>Asset Protection Trusts<span class="sep">·</span>Business Succession Planning</li>
      <li>LLC Law<span class="sep">·</span>Estate Planning<span class="sep"></span>Medicaid Planning</li>
    </ul>
    <div class="card__rule"></div>
    <p class="card__contact">123 Lorem ipsum dolor, consectetur, City 1234 &nbsp;·&nbsp; email martin@halepa.com &nbsp;·&nbsp; Phone +123456</p>
  </section>

  <section class="mark-display" aria-label="Monogram mark">
    <div class="mark-display__square"></div>
    <span class="mark-display__initials">MH</span>
  </section>
</body>
</html>
```